Astrological planner&diary book cover.

Book cover for print paperback. Title: "Whole Stargazer Journal & Logbook – Sign One (Sign Two, Sign Three etc) 2022: Shape your days by charting Orbital and Night angles and passages, Idle Drift, Night cycles, Sky almanac, and Reversing bodies." The book is a series of Astrological diary & planner for 2022 for each Zodiac sign (12 books in total). The design template should be the same – the only difference would be the Zodiac sign image and text.
It should be neutral to positive. There is no restriction regarding the colors – it can be both B&W and full color.
The design should be original and not include any images which require obtaining a copyright license to use. Symbols in common use and not copyrighted are probably ok.
Text for the back cover is not yet available, will be ready by the end of the project. I will need PDF, JPEG, TIFF (all formats both in CMYK and RGB), and the source file. For CMYK, we need files with no color profiles assigned.
I have several options in my mind (But please do not limit yourself by these options - please feel free to suggest your vision):
1) Is Gradient morning clear sky and the star constellation and image at skyrise (like a rising star)
2) solid dark color with image and symbols of the Zodiac sign
75% of my auditory are women

```html
<!DOCTYPE html>
<html lang="en">
<head>
<meta charset="utf-8">
<title>Whole Stargazer Journal &amp; Logbook 2022 – Cover</title>
<link rel="stylesheet" href="https://fonts.googleapis.com/css2?family=Uncial+Antiqua&family=Playfair+Display:wght@400&family=Libre+Caslon+Text&display=swap">
<style>
  :root {
    --page-bg: #0c1238;
    --sky-top: #12164f;
    --sky-upper: #1d2378;
    --sky-mid: #2c3fae;
    --sky-glow: #4f8fe0;
    --horizon-pink: #f0bcd8;
    --horizon-lilac: #9aa6e6;
    --hill: #0b0b1c;
    --ink-light: #ffffff;
    --ink-soft: #eef2ff;
    --wheel-core: #d9ecff;
    --wheel-mid: #5fa6f0;
  }
  * { box-sizing: border-box; margin: 0; padding: 0; }
  html, body {
    width: 1200px;
    height: 1200px;
    overflow: hidden;
    background: var(--page-bg);
  }
  .cover {
    position: absolute;
    left: 226px;
    top: 40px;
    width: 747px;
    height: 1120px;
    overflow: hidden;
    background: linear-gradient(180deg,
      var(--sky-top) 0%,
      var(--sky-upper) 30%,
      var(--sky-mid) 58%,
      var(--sky-glow) 78%,
      var(--horizon-lilac) 83%,
      var(--horizon-pink) 87%,
      var(--hill) 93%,
      var(--hill) 100%);
    color: var(--ink-light);
  }
  .title {
    position: absolute;
    font-family: "Uncial Antiqua", serif;
    color: var(--ink-light);
    text-shadow: 1px 2px 3px rgba(0, 0, 0, 0.45);
    line-height: 1;
    white-space: nowrap;
  }
  .title-first { left: 92px; top: 36px; font-size: 92px; }
  .title-year  { left: 560px; top: 128px; font-size: 44px; }
  .title-main  { left: 44px; top: 150px; font-size: 106px; letter-spacing: -1px; }
  .title-sub   { left: 46px; top: 262px; font-size: 38px; }
  .title-signs {
    position: absolute;
    left: 442px;
    top: 283px;
    font-family: "Uncial Antiqua", serif;
    font-size: 13px;
    color: var(--ink-soft);
    white-space: nowrap;
  }
  .divider {
    position: absolute;
    left: 253px;
    top: 336px;
    width: 262px;
    height: 12px;
  }
  .subtitle {
    position: absolute;
    left: 40px;
    top: 360px;
    width: 667px;
    font-family: "Libre Caslon Text", serif;
    font-size: 20px;
    line-height: 34px;
    text-align: center;
    color: var(--ink-light);
    letter-spacing: -0.3px;
  }
  .artwork {
    position: absolute;
    left: 140px;
    top: 500px;
    width: 470px;
    height: 560px;
    border-radius: 50% 50% 10px 10px;
    background: radial-gradient(circle at 50% 34%,
      var(--wheel-core) 0%,
      var(--wheel-mid) 14%,
      rgba(80, 140, 230, 0.35) 38%,
      rgba(60, 90, 200, 0) 62%);
  }
  .author {
    position: absolute;
    left: 0;
    top: 1048px;
    width: 100%;
    text-align: center;
    font-family: "Playfair Display", serif;
    font-size: 34px;
    letter-spacing: 1px;
    color: var(--ink-light);
    text-transform: uppercase;
  }
</style>
</head>
<body>
  <main class="cover">
    <h1 class="title-block">
      <span class="title title-first">Whole</span>
      <span class="title title-year">2022</span>
      <span class="title title-main">Stargazer</span>
      <span class="title title-sub">Journal &amp; Logbook</span>
      <span class="title-signs">Sign One (Sign Two, Sign Three etc)</span>
    </h1>

    <svg class="divider" viewBox="0 0 262 12" aria-hidden="true">
      <line x1="0" y1="6" x2="118" y2="6" stroke="#ffffff" stroke-width="1.5"/>
      <circle cx="131" cy="6" r="5" fill="#ffffff"/>
      <line x1="144" y1="6" x2="262" y2="6" stroke="#ffffff" stroke-width="1.5"/>
    </svg>

    <p class="subtitle">Shape your days by charting Orbital and Night angles and passages, Idle Drift, Night cycles, Sky almanac, and Reversing bodies.</p>

    <div class="artwork" role="img" aria-label="Glowing zodiac wheel around a full moon among constellations, above a woman silhouetted with raised arms on a hilltop at dawn"></div>

    <p class="author">Marla Quinlan</p>
  </main>
</body>
</html>
```